Logo is done, need templates now

I want to be able to have an email template, same for word documents, powerpoint etc. I have the logo, now I need all the pieces for appearance in correspondence and marketing

Target Market(s)

Professional Advisors and Wealthy Clients

Font styles to use
Serif

Requirements
Must have
• I want to be able to do word documents and email them with letterhead. I need great email signatures. I need similar formatting for the word documents to be flexible to add to powerpoint and other presentations.

```html
<!DOCTYPE html>
<html lang="en">
<head>
<meta charset="utf-8">
<title>Quietmoor Capital Letterhead</title>
<link href="https://fonts.googleapis.com/css2?family=Questrial&display=swap" rel="stylesheet">
<style>
  :root {
    --backdrop: #e1e1e1;
    --paper: #ffffff;
    --paper-fade: #f4f4f4;
    --ink: #111111;
    --ink-body: #5a5a5a;
    --ink-heading: #4a4a4a;
    --signature-tone: #d6d9de;
  }
  * { box-sizing: border-box; margin: 0; padding: 0; }
  html, body {
    width: 1029px; height: 1200px; overflow: hidden;
    background: var(--backdrop);
    font-family: "Questrial", "Century Gothic", sans-serif;
  }
  .letterhead {
    position: absolute; left: 152px; top: 90px;
    width: 722px; height: 1017px;
    background: linear-gradient(90deg, var(--paper) 0%, var(--paper) 30%, var(--paper-fade) 100%);
  }
  .brand {
    position: absolute; left: 62px; top: 112px;
    font-size: 15px; letter-spacing: 3px; color: var(--ink);
    white-space: nowrap; display: flex; align-items: center; gap: 8px;
  }
  .brand-dot { width: 8px; height: 8px; background: var(--ink); border-radius: 50%; }
  .contact {
    position: absolute; right: 57px; top: 64px;
    list-style: none; text-align: right;
    font-size: 11px; line-height: 13.4px; color: var(--ink);
  }
  .contact li { display: flex; justify-content: flex-end; align-items: flex-start; gap: 8px; margin-bottom: 1.5px; }
  .contact li.address { margin-bottom: 3px; }
  .contact svg { width: 10px; height: 11px; flex: none; margin-top: 1px; }
  .greeting {
    position: absolute; left: 62px; top: 284px;
    font-size: 19px; font-weight: 400; color: var(--ink-heading);
  }
  .body-copy {
    position: absolute; left: 62px; top: 338px; width: 599px;
    font-size: 10.4px; line-height: 15.45px; color: var(--ink-body);
    text-align: justify; hyphens: auto;
  }
  .body-copy p { margin-bottom: 15.45px; }
  .closing {
    position: absolute; left: 62px; top: 665px;
    font-size: 10.4px; color: var(--ink-body);
  }
  .signature {
    position: absolute; left: 62px; top: 707px;
    width: 85px; height: 36px; background: var(--signature-tone);
  }
</style>
</head>
<body>
  <main class="letterhead">
    <div class="brand"><span class="brand-dot"></span>QUIETMOOR CAPITAL</div>

    <ul class="contact">
      <li class="address"><span>1420 Larkspur Court<br>Juneau, Alaska 99801</span>
        <svg viewBox="0 0 10 12"><path d="M5 0.5a4 4 0 0 0-4 4c0 3 4 7 4 7s4-4 4-7a4 4 0 0 0-4-4z" fill="var(--ink)"/><circle cx="5" cy="4.5" r="1.5" fill="var(--paper)"/></svg></li>
      <li><span>555-014-2276</span>
        <svg viewBox="0 0 10 12"><path d="M2 1.5l2 0 1 2.5-1.3 1a6 6 0 0 0 2.8 2.8l1-1.3 2.5 1v2a1 1 0 0 1-1 1A8 8 0 0 1 1 2.5a1 1 0 0 1 1-1z" fill="var(--ink)"/></svg></li>
      <li><span>hello@quietmoorcapital.com</span>
        <svg viewBox="0 0 10 12"><rect x="0.5" y="3" width="9" height="6.5" fill="var(--ink)"/><path d="M0.8 3.3L5 6.6l4.2-3.3" stroke="var(--paper)" stroke-width="0.8" fill="none"/></svg></li>
      <li><span>www.quietmoorcapital.com</span>
        <svg viewBox="0 0 10 12"><circle cx="5" cy="6" r="4.3" fill="var(--ink)"/><path d="M2.5 4.5c1 0 1.5 1 2.5 1s0 2 1 2.5M6 2.5c0 1 1 1.5 2 1.5" stroke="var(--paper)" stroke-width="0.8" fill="none"/></svg></li>
    </ul>

    <h1 class="greeting">Dear Mr. Harlan,</h1>

    <section class="body-copy">
      <p>Lorem ipsum dolor sit amet, consectetur adipiscing elit. Donec orci purus, luctus vitae dignissim eu, iaculis sed purus. Vivamus faucibus, ipsum nec aliquet viverra, leo mauris condimentum ligula, sit amet sagittis enim ligula quis arcu. Nam egestas tortor id nisi porttitor mattis. In tortor ante, ultricies in suscipit a, tempus non massa. Vivamus et auctor mi. Fusce vel massa nulla. Phasellus nec eros mauris, et scelerisque orci.</p>
      <p>Donec malesuada orci vitae nulla accumsan porta a id massa. Quisque accumsan iaculis magna sit amet fringilla. Maecenas consequat, magna eget tincidunt semper, odio nibh rutrum mi, id feugiat ante nisi eu risus. Vestibulum nunc orci, rhoncus a placerat in, ultricies in mi. Cras mattis varius eros, vel fringilla nisi suscipit eget. Quisque scelerisque sagittis nulla at porttitor.</p>
      <p>Sed id augue vitae urna euismod commodo aliquet a quam. Pellentesque arcu velit, cursus et malesuada ut, consequat et diam. Nullam erat sem, rhoncus id ullamcorper vitae, rhoncus et arcu. In ultricies ultricies nulla, ut rutrum nisi iaculis at. Donec eu magna a metus ornare faucibus. Fusce aliquet faucibus ultricies. Morbi semper, est id tincidunt gravida, sem arcu adipiscing lacus, ac bibendum nulla leo eu purus. Quisque nec diam sed risus consectetur a ccumsan quis quis nibh. Vestibulum id purus lorem.</p>
      <p>It is a long established fact that a reader will be distracted by the readable content of a page when looking at its layout. The point of using Lorem Ipsum is that it has a more-or-less normal distribution of letters, as opposed to using 'Content here, content here', making it look like readable English. Many desktop publishing packages</p>
    </section>

    <p class="closing">Sincerely,</p>
    <div class="signature" role="img" aria-label="Handwritten signature of the sender"></div>
  </main>
</body>
</html>
```